Organic Food company needs a new design label logo

Our company name is Brackwell Dene Organic. We pack organic dried products and sell to natural, organic or small supermarkets in the UK.

We would like to you to design our new label with logo.

The label size should be the width is 65 mm and the length is 85 mm. The label should also include our land stewardship guild and European organic logos.

The food label should reflect our company that we are organic and we sell quality organic food products.

The colours should be pastel and warm colour. It shouldn’t have so many colour.
Updates

Dear All,

Just let you know that this project is food label with the new design. The size of the label should as follow; 
width: 65 mm
length: 85 mm

It will be used for dried fruit, vegetables and nuts. so the middle of the label should be blank, as the print shop will print the name separetly.

When you design our new logo label, please also read my previous note.

Thank you.

Target Market(s)

Above 25 years old. People who like to buy organic or natural food products. Middle income people.

Industry/Entity Type

It Company

Requirements
Must have
• 1) Land Stewardship Guild logo (attached as file )

2) European organic logo ( can be download from http://farmmark-register.example/produce/natural/seal-policy/badge_en )

3) The following information should be either next to or underneath to European logo;
XK-CRT-17
Non-EU Agriculture

The above text information shouldn't be very big.

4) There should be enough space in the middle of the label to write (later by the print shop) full product name and weight.

5) Our company name is "Brackwell Dene Organic"

6) Our web site address is www.brackwelldene.example

```html
<!DOCTYPE html>
<html lang="en">
<head>
<meta charset="utf-8">
<title>Brackwell Dene Organic – Product Labels</title>
<link href="https://fonts.googleapis.com/css2?family=Fira+Sans:wght@400;600&family=Sue+Ellen+Francisco&display=swap" rel="stylesheet">
<style>
  :root {
    --page: #ffffff;
    --label: #323a3a;
    --ink-light: #e9ece6;
    --ink-muted: #c9cec8;
    --orange: #f08a24;
    --yellow: #f3c320;
    --peach: #f0b36a;
    --eu-green: #7bb534;
    --seal: #8a918c;
  }
  * { margin: 0; padding: 0; box-sizing: border-box; }
  html, body {
    width: 1200px; height: 586px; overflow: hidden;
    background: var(--page);
  }
  .label-range {
    position: relative; width: 1200px; height: 586px;
  }
  .label {
    position: absolute; top: 226px;
    width: 132px; height: 172px;
    background: var(--label);
    border-radius: 7px;
    font-family: "Fira Sans", sans-serif;
    color: var(--ink-light);
  }
  .label--vegetable { left: 338px; --accent: var(--orange); }
  .label--apricot   { left: 535px; --accent: var(--yellow); }
  .label--nuts      { left: 733px; --accent: var(--peach); }

  .brand {
    position: absolute; top: 22px; left: 0; right: 0;
    text-align: center; color: var(--accent);
    font-weight: 600; line-height: 1.05;
  }
  .brand__dot {
    display: block; width: 16px; height: 16px; margin: 0 auto 4px;
    border-radius: 50%; background: var(--accent);
  }
  .brand__name { display: block; font-size: 14px; }
  .brand__sub { display: block; font-size: 11px; }

  .product {
    position: absolute; top: 100px; left: 0; right: 0; text-align: center;
  }
  .product__name {
    font-family: "Sue Ellen Francisco", cursive;
    font-size: 13px; color: var(--ink-light); line-height: 1;
  }
  .product__weight {
    font-size: 5.5px; color: var(--ink-muted); margin-top: 3px;
  }

  .certs {
    position: absolute; left: 8px; right: 8px; bottom: 10px;
    display: flex; align-items: flex-end; gap: 5px;
  }
  .eu-mark { display: flex; flex-direction: column; align-items: center; }
  .eu-mark__badge {
    width: 18px; height: 12px; background: var(--eu-green); border-radius: 1px;
  }
  .eu-mark__code { font-size: 3.4px; margin-top: 1px; color: var(--ink-light); }
  .eu-mark__origin { font-size: 2.6px; color: var(--ink-muted); }
  .guild-seal { width: 15px; height: 15px; margin-bottom: 2px; }
  .web {
    margin-left: auto; margin-bottom: 6px;
    font-size: 5.3px; color: var(--ink-light); white-space: nowrap;
  }
</style>
</head>
<body>
<main class="label-range">

  <section class="label label--vegetable">
    <div class="brand"><span class="brand__dot"></span><span class="brand__name">Brackwell Dene</span><span class="brand__sub">Organic</span></div>
    <div class="product"><p class="product__name">Vegetable</p><p class="product__weight">150gm</p></div>
    <div class="certs">
      <div class="eu-mark"><span class="eu-mark__badge" role="img" aria-label="European organic certification badge"></span><span class="eu-mark__code">XK-CRT-17</span><span class="eu-mark__origin">Non-EU Agriculture</span></div>
      <svg class="guild-seal" viewBox="0 0 16 16" role="img" aria-label="Land Stewardship Guild seal"><circle cx="8" cy="8" r="7" fill="none" stroke="var(--seal)" stroke-width="1.4"/></svg>
      <span class="web">www.brackwelldene.example</span>
    </div>
  </section>

  <section class="label label--apricot">
    <div class="brand"><span class="brand__dot"></span><span class="brand__name">Brackwell Dene</span><span class="brand__sub">Organic</span></div>
    <div class="product"><p class="product__name">Dried Apricots</p><p class="product__weight">150gm</p></div>
    <div class="certs">
      <div class="eu-mark"><span class="eu-mark__badge" role="img" aria-label="European organic certification badge"></span><span class="eu-mark__code">XK-CRT-17</span><span class="eu-mark__origin">Non-EU Agriculture</span></div>
      <svg class="guild-seal" viewBox="0 0 16 16" role="img" aria-label="Land Stewardship Guild seal"><circle cx="8" cy="8" r="7" fill="none" stroke="var(--seal)" stroke-width="1.4"/></svg>
      <span class="web">www.brackwelldene.example</span>
    </div>
  </section>

  <section class="label label--nuts">
    <div class="brand"><span class="brand__dot"></span><span class="brand__name">Brackwell Dene</span><span class="brand__sub">Organic</span></div>
    <div class="product"><p class="product__name">Nuts</p><p class="product__weight">150gm</p></div>
    <div class="certs">
      <div class="eu-mark"><span class="eu-mark__badge" role="img" aria-label="European organic certification badge"></span><span class="eu-mark__code">XK-CRT-17</span><span class="eu-mark__origin">Non-EU Agriculture</span></div>
      <svg class="guild-seal" viewBox="0 0 16 16" role="img" aria-label="Land Stewardship Guild seal"><circle cx="8" cy="8" r="7" fill="none" stroke="var(--seal)" stroke-width="1.4"/></svg>
      <span class="web">www.brackwelldene.example</span>
    </div>
  </section>

</main>
</body>
</html>
```